Homepage design for personal injury lawyer

NOTE: I will not close the project until June 9th. I want to give everyone time to put in their best work.
Your task is to redesign the homepage for this site:
https://corwistlane.com/
Feel free to use any images you find on the site.
I'm deliberately leaving the description simple so that I don't limit you.
Updates
Hi everyone. I will keep the project open for a few days to leave time for designs.
Number of Pages Required
1 page
Look and feel
Each slider illustrates characteristics of the customer's brand and the style your logo design should communicate.

```html
<!DOCTYPE html>
<html lang="en">
<head>
<meta charset="utf-8">
<title>Corwist Lane – Phoenix Personal Injury Lawyers</title>
<link rel="stylesheet" href="https://fonts.googleapis.com/css2?family=Open+Sans:wght@400;600;700&family=Noto+Serif:wght@700&family=Oswald:wght@500&display=swap">
<style>
  :root {
    --ink: #1c2540;
    --grey: #6b6f78;
    --nav: #5e636c;
    --brand-blue: #3b6fb0;
    --white: #ffffff;
    --hero-dark: #0f141c;
    --hero-mid: #2a2f38;
    --hero-light: #4a505c;
    --line: #7c8088;
  }
  * { box-sizing: border-box; margin: 0; padding: 0; }
  html, body { width: 1200px; height: 865px; overflow: hidden; background: var(--white); }
  body { position: relative; font-family: "Open Sans", sans-serif; color: var(--ink); }

  .site-header { position: absolute; left: 0; top: 0; width: 1200px; height: 120px; }
  .brand { position: absolute; left: 58px; top: 50px; display: flex; align-items: center; gap: 10px; text-decoration: none; }
  .brand-dot { width: 40px; height: 40px; border-radius: 50%; background: var(--brand-blue); }
  .brand-name { font-size: 26px; font-weight: 600; color: var(--grey); letter-spacing: 0.5px; }

  .main-nav { position: absolute; left: 429px; top: 58px; display: flex; gap: 23px; }
  .main-nav a { font-size: 14px; font-weight: 600; color: var(--nav); text-decoration: none; display: flex; align-items: center; gap: 3px; white-space: nowrap; }
  .main-nav svg { width: 7px; height: 5px; margin-top: 4px; }

  .call-button { position: absolute; left: 973px; top: 46px; width: 170px; height: 49px; border: 1.5px solid var(--line); border-radius: 25px; text-align: center; color: var(--nav); text-decoration: none; }
  .call-label { display: block; font-size: 8.5px; font-weight: 600; margin-top: 8px; }
  .call-number { display: block; font-size: 19px; font-weight: 700; line-height: 1.1; }

  .hero { position: absolute; left: 50px; top: 141px; width: 1102px; height: 577px; border-radius: 50px; overflow: hidden; color: var(--white); }
  .hero-photo { position: absolute; inset: 0; background: linear-gradient(100deg, var(--hero-dark) 0%, var(--hero-mid) 45%, var(--hero-light) 80%, #5a5f6a 100%); }
  .hero-rule { position: absolute; left: 68px; top: 120px; width: 339px; height: 2px; background: var(--white); }
  .hero-kicker { position: absolute; left: 66px; top: 145px; width: 530px; font-size: 16.5px; line-height: 20px; color: var(--white); }
  .hero-title { position: absolute; left: 64px; top: 205px; width: 640px; font-family: "Noto Serif", serif; font-weight: 700; font-size: 60px; line-height: 62px; color: var(--white); }
  .hero-text { position: absolute; left: 67px; top: 358px; width: 530px; font-size: 16.5px; line-height: 20px; color: var(--white); }
  .hero-cta { position: absolute; left: 64px; top: 456px; width: 285px; height: 55px; border: 2px solid var(--white); border-radius: 28px; color: var(--white); text-decoration: none; font-family: "Noto Serif", serif; font-weight: 700; font-size: 20px; display: flex; align-items: center; padding-left: 27px; gap: 20px; }

  .stats { position: absolute; left: 0; top: 762px; width: 1200px; }
  .stat { position: absolute; top: 0; }
  .stat-figure { height: 40px; font-family: "Noto Serif", serif; font-weight: 700; font-size: 36px; line-height: 40px; color: var(--ink); white-space: nowrap; }
  .stat-label { font-family: "Oswald", sans-serif; font-weight: 500; font-size: 16px; line-height: 1; margin-left: 6px; letter-spacing: 0.2px; }
  .stat-note { font-size: 12px; color: var(--grey); margin-top: 2px; white-space: nowrap; }
  .stat-rate { left: 56px; }
  .stat-reviews { left: 326px; }
  .stat-fee { left: 594px; }

  .highlight-box { position: absolute; left: 882px; top: 757px; width: 271px; height: 73px; border: 2px solid var(--line); border-radius: 10px; padding: 10px 0 0 18px; }
  .highlight-kicker { font-size: 12px; color: var(--grey); line-height: 14px; }
  .highlight-title { font-family: "Noto Serif", serif; font-weight: 700; font-size: 32px; line-height: 38px; color: var(--ink); }
</style>
</head>
<body>
  <header class="site-header">
    <a class="brand" href="https://corwistlane.com/">
      <span class="brand-dot"></span>
      <span class="brand-name">Corwist Lane</span>
    </a>
    <nav class="main-nav">
      <a href="#">About Us <svg viewBox="0 0 7 5"><path d="M0 0h7L3.5 5z" fill="currentColor"/></svg></a>
      <a href="#">Case We Handle <svg viewBox="0 0 7 5"><path d="M0 0h7L3.5 5z" fill="currentColor"/></svg></a>
      <a href="#">Location <svg viewBox="0 0 7 5"><path d="M0 0h7L3.5 5z" fill="currentColor"/></svg></a>
      <a href="#">Resources <svg viewBox="0 0 7 5"><path d="M0 0h7L3.5 5z" fill="currentColor"/></svg></a>
      <a href="#">Contact Us</a>
    </nav>
    <a class="call-button" href="tel:6025550148">
      <span class="call-label">Call 24/7 for Free Consultation</span>
      <span class="call-number">602-555-0148</span>
    </a>
  </header>

  <section class="hero">
    <div class="hero-photo" role="img" aria-label="Photo of an attorney in a tweed jacket consulting with a couple seated in an office"></div>
    <div class="hero-rule"></div>
    <p class="hero-kicker">Lorem ipsum dolor sit amet, consectetuer adipiscing elit, sed diam nonummy nibh euismod tincidunt ut laoreet dolore magna aliquam</p>
    <h1 class="hero-title">Phoenix Personal Injury Lawyers</h1>
    <p class="hero-text">Ltt, sed diam nonummy nibh euismod tincidunt ut laoreet dolore magna aliquam erat volutpat. Ut wisi enim ad minim veniam, quis nostrud exerci tation ullamcorper suscipit lobortis nisl ut aliquip ex</p>
    <a class="hero-cta" href="#">Free Consultation
      <svg width="40" height="26" viewBox="0 0 40 26"><path d="M1 13h36M26 2l11 11-11 11" fill="none" stroke="currentColor" stroke-width="2"/></svg>
    </a>
  </section>

  <section class="stats">
    <div class="stat stat-rate">
      <div class="stat-figure">99%<span class="stat-label">SUCCESS RATE</span></div>
      <p class="stat-note">Lorem ipsum dolor sit amet, consectetuer</p>
    </div>
    <div class="stat stat-reviews">
      <div class="stat-figure">550+<span class="stat-label">5-STAR REVIEWS</span></div>
      <p class="stat-note">Lorem ipsum dolor sit amet, consectetuer</p>
    </div>
    <div class="stat stat-fee">
      <div class="stat-figure">$0 Fee</div>
      <p class="stat-note">Lorem ipsum dolor sit amet, consectetuer</p>
    </div>
  </section>

  <div class="highlight-box">
    <p class="highlight-kicker">Lorem ipsum dolor sit amet</p>
    <p class="highlight-title">Lorem ipsum</p>
  </div>
</body>
</html>
```